"Torvela" (spanish restaurant) "Bar de Tapas"

"Torvela" is a spanish restaurant located in the city of Santo Domingo, Dominican Republic. It needs a new and fresh idea for its business card. I would like to take the idea of one of the spaces of the restaurant represented on a business card, for example, the blue and emblematic entrance door of the restaurant, or maybe the bricks on the main room of the restaurant, or how about the bar. Any idea it's good! I invite all the creative designers to participate on the suggestions of it.

What doe sit need? It needs this information on it:

Name: Torvela
Business: Restaurante
Address: Calle Benito Sorel 00, Las Quintas
Phone number: 809-000-0000
website: www.torvelarestaurante.example

Reason: NEED MORE OPTION FOR IT. I WANT YOU TO EXPRESS YOUR DESIGN AS YOU WANT TO NOT AS I ASK YOU TO.

Industry/Entity Type

Restaurant

Contact Information for Business Card

c/Benito Sorel 47

Requirements
Must have
• Creativity. I'm open to new and fresh ideas.
Nice to have
• The entrance door (blue one) would be a plus in the design of the card. Maybe the background could be images of materials like bricks or wood, like the ones in the pictures of the restaurant.

```html
<!DOCTYPE html>
<html lang="es">
<head>
<meta charset="utf-8">
<title>Torvela Restaurante – Business Card</title>
<link rel="stylesheet" href="https://fonts.googleapis.com/css2?family=Tinos:wght@400;700&display=swap">
<style>
  :root {
    --page-bg: #e9e5df;
    --card-white: #ffffff;
    --brand-gold: #9a8a5c;
    --ink: #2a2622;
    --ink-soft: #4a443d;
    --photo-dark: #1f2a22;
    --photo-mid: #4b5a3e;
    --photo-warm: #c89a5a;
    --photo-light: #efe0bf;
  }
  * { box-sizing: border-box; margin: 0; padding: 0; }
  html, body {
    width: 1200px;
    height: 900px;
    overflow: hidden;
    background: var(--page-bg);
  }
  .sheet {
    width: 1200px;
    height: 900px;
    display: flex;
    flex-direction: column;
    align-items: center;
    justify-content: center;
    gap: 40px;
  }
  .card {
    width: 630px;
    height: 360px;
    position: relative;
    overflow: hidden;
    box-shadow: 0 6px 18px rgba(0,0,0,0.18);
  }

  /* Brand name placeholder: one font, one weight, one colour, plain square */
  .brand {
    display: flex;
    align-items: center;
    gap: 14px;
    font-family: "Tinos", serif;
    font-weight: 400;
    color: var(--brand-gold);
    white-space: nowrap;
  }
  .brand-square {
    width: 18px;
    height: 18px;
    background: var(--brand-gold);
    flex: none;
  }

  /* Front */
  .card--front { background: var(--photo-dark); }
  .card-photo {
    position: absolute;
    inset: 0;
    background:
      radial-gradient(ellipse at 30% 75%, rgba(239,224,191,0.55), transparent 45%),
      radial-gradient(ellipse at 80% 30%, rgba(200,154,90,0.5), transparent 40%),
      linear-gradient(160deg, var(--photo-mid) 0%, var(--photo-dark) 55%, #3a2e22 100%);
  }
  .front-brand {
    position: absolute;
    left: 50%;
    top: 50%;
    transform: translate(-50%, -50%);
    font-size: 72px;
    line-height: 1;
  }

  /* Back */
  .card--back {
    background: var(--card-white);
    display: flex;
    align-items: center;
    justify-content: space-between;
    padding: 0 36px 0 40px;
  }
  .back-brand {
    font-size: 50px;
    line-height: 1;
  }
  .contact {
    font-family: "Tinos", serif;
    color: var(--ink-soft);
    font-size: 13px;
    line-height: 1.45;
    white-space: nowrap;
  }
  .contact-name {
    font-family: "Tinos", serif;
    font-weight: 400;
    font-size: 24px;
    line-height: 1.1;
    color: var(--brand-gold);
  }
  .contact-business {
    font-weight: 700;
    color: var(--ink);
    margin-bottom: 2px;
  }
</style>
</head>
<body>
<main class="sheet">
  <section class="card card--front">
    <div class="card-photo" role="img" aria-label="Night photo of the restaurant terrace with palm trees, warm lights and an awning"></div>
    <p class="brand front-brand"><span class="brand-square"></span>Torvela</p>
  </section>

  <section class="card card--back">
    <p class="brand back-brand"><span class="brand-square"></span>Torvela</p>
    <div class="contact">
      <p class="contact-name">Torvela</p>
      <p class="contact-business">Restaurante</p>
      <p>Address: Calle Benito Sorel 00, Las Quintas</p>
      <p>Phone number: 809-000-0000</p>
      <p>website: www.torvelarestaurante.example</p>
    </div>
  </section>
</main>
</body>
</html>
```